rosie's empada

We are a family business based in sydney introducing a common brazilian street food into sydney cafes and restaurants.
what we provide are pastels which is a thinly crust pie with assorted fillings
we mainly focus on supplying cafes and restaurants but we do sell privately.
We have had a few cafes ask to stock our cards due to customer request. except we don't have any!! hence why we need you. : )
I have attached an image of our pastels which is just to give you an idea of what they look like.
Updates
I have just seen all the designs and am impressed by some of your work. I will have to sit with my parter later today and will hopefully have some more constructive feedback and a decision soon.
Hello designers,
Hello designers,
Target Market(s)
cafe's and restaurants
Industry/Entity Type
Business
Contact Information for Business Card
Rosie's empada
joaquim 0428716904
rosiesempada@fernmail.com

```html
<!DOCTYPE html>
<html lang="en">
<head>
<meta charset="utf-8">
<title>Rosie's empada – Business Card</title>
<link href="https://fonts.googleapis.com/css2?family=Jost:wght@500;600&display=swap" rel="stylesheet">
<style>
  :root {
    --backdrop: #f2f2f2;
    --card: #15181b;
    --gold: #c09a5b;
    --white: #ffffff;
    --ink-soft: #f1f1f1;
  }
  * { margin: 0; padding: 0; box-sizing: border-box; }
  html, body {
    width: 1200px;
    height: 1000px;
    overflow: hidden;
    background: var(--backdrop);
  }
  .business-card {
    position: absolute;
    left: 142px;
    top: 224px;
    width: 915px;
    height: 559px;
    background: var(--card);
    font-family: "Jost", "Futura", sans-serif;
  }
  .brand {
    position: absolute;
    left: 30px;
    right: 0;
    top: 60px;
    height: 340px;
    display: flex;
    align-items: center;
    justify-content: center;
    gap: 28px;
  }
  .brand-dot {
    width: 92px;
    height: 92px;
    border-radius: 50%;
    background: var(--gold);
    flex: none;
  }
  .brand-name {
    font-size: 86px;
    font-weight: 600;
    color: var(--white);
    letter-spacing: 0.5px;
    line-height: 1;
    white-space: nowrap;
  }
  .contact-list {
    position: absolute;
    left: 68px;
    top: 403px;
    list-style: none;
  }
  .contact-item {
    display: flex;
    align-items: center;
    height: 48px;
    color: var(--ink-soft);
    font-size: 21px;
    font-weight: 600;
    letter-spacing: 0.3px;
  }
  .contact-icon {
    width: 28px;
    height: 30px;
    margin-right: 21px;
    flex: none;
  }
  .contact-icon * {
    fill: none;
    stroke: var(--ink-soft);
    stroke-width: 2;
    stroke-linejoin: round;
    stroke-linecap: round;
  }
</style>
</head>
<body>
  <section class="business-card">
    <div class="brand">
      <span class="brand-dot"></span>
      <span class="brand-name">Rosie's empada</span>
    </div>

    <ul class="contact-list">
      <li class="contact-item">
        <svg class="contact-icon" viewBox="0 0 28 30" aria-hidden="true">
          <path d="M8 4 L12 4 L14 10 L11 12 C12.5 16 15 18.5 18 20 L20 17 L26 19 L26 23 C26 25 24.5 26 22.5 26 C13 25 5 17 4 7.5 C4 5.5 5.5 4 8 4 Z"/>
        </svg>
        <span class="contact-text">Phone: Joaquim - 0428716904</span>
      </li>
      <li class="contact-item">
        <svg class="contact-icon" viewBox="0 0 28 30" aria-hidden="true">
          <rect x="2.5" y="7" width="23" height="16" rx="2"/>
          <path d="M3 8 L14 17 L25 8"/>
        </svg>
        <span class="contact-text">Email: rosiesempada@fernmail.com</span>
      </li>
    </ul>
  </section>
</body>
</html>
```